Soy Candle Business needs a label design

We need a label design for a new company selling soy candles - Velvet Hearth Co.

We are using apothecary jars in 3 sizes.
As per attached candles will be dressed with a beautiful black bow and all finished with a diamante in centre of bow.

We would like label done on lid of candle jars - 5cm circle (5cm from one side to the other), this way one label will fit each product size. Label will be done as a sticker.

We are thinking of the background colour to be black, however are open to recommendations. We want label to be classy, elegant and simple.

Inspiration for candle design came from attached invitation that features the bow, and beautiful vintage paper on top area.

Label should include the following 3 pieces of information:
Velvet Hearth Co (company name)
Coconut Lime (this will change depending on fragrance)
Soy Candle

Velvet Hearth Co does not have a company logo... what is done for the label will set tone for what is done across other elements of business moving forward.

Industry/Entity Type

Business

Requirements
Must have
• Velvet Hearth Co
Fragrance Flavour
Soy Candle

```html
<!DOCTYPE html>
<html lang="en">
<head>
<meta charset="utf-8">
<title>Velvet Hearth Co — Soy Candle Label</title>
<link rel="stylesheet" href="https://fonts.googleapis.com/css2?family=Didact+Gothic&family=Open+Sans:wght@400&display=swap">
<style>
  :root {
    --paper: #ffffff;
    --label-black: #000000;
    --ring-grey: #9a9a9a;
    --caption-ink: #111111;
    --scent-lime: #7fff00;
    --scent-magenta: #ee10e6;
    --scent-yellow: #ffee00;
    --scent-sky: #38c8f2;
    --scent-orange: #ff9d1e;
  }
  html, body {
    margin: 0;
    padding: 0;
    width: 1200px;
    height: 823px;
    overflow: hidden;
    background: var(--paper);
  }
  .presentation-board {
    display: block;
    width: 1200px;
    height: 823px;
  }
  .label-face { fill: var(--label-black); stroke: currentColor; }
  .brand-name {
    font-family: "Didact Gothic", sans-serif;
    fill: currentColor;
  }
  .product-type {
    font-family: "Didact Gothic", sans-serif;
    fill: currentColor;
  }
  .scent-ring {
    font-family: "Didact Gothic", sans-serif;
    fill: var(--ring-grey);
  }
  .caption {
    font-family: "Open Sans", sans-serif;
    font-size: 13px;
    letter-spacing: 1.6px;
    fill: var(--caption-ink);
  }
  .colourway-magenta { color: var(--scent-magenta); }
  .colourway-yellow { color: var(--scent-yellow); }
  .colourway-sky { color: var(--scent-sky); }
  .colourway-orange { color: var(--scent-orange); }
  .colourway-lime { color: var(--scent-lime); }
</style>
</head>
<body>
<svg class="presentation-board" viewBox="0 0 1200 823" xmlns="http://www.w3.org/2000/svg">
  <defs>
    <path id="small-ring-path" d="M -80 0 A 80 80 0 1 1 80 0 A 80 80 0 1 1 -80 0"/>
    <path id="large-ring-path" d="M -238 0 A 238 238 0 1 1 238 0 A 238 238 0 1 1 -238 0"/>

    <symbol id="scent-label" viewBox="-100 -100 200 200">
      <circle class="label-face" cx="0" cy="0" r="97" stroke-width="4"/>
      <text class="scent-ring" font-size="9.5" letter-spacing="1">
        <textPath href="#small-ring-path" textLength="500">scent scent scent scent scent scent scent scent scent scent scent scent scent scent scent scent</textPath>
      </text>
      <text class="brand-name" x="4" y="-8" font-size="17" text-anchor="middle">Velvet Hearth Co</text>
      <text class="product-type" x="4" y="22" font-size="10" text-anchor="middle">soy candle</text>
    </symbol>

    <symbol id="logo-mark" viewBox="-100 -100 200 200">
      <circle class="label-face" cx="0" cy="0" r="97" stroke-width="4"/>
      <text class="brand-name" x="0" y="-6" font-size="18" text-anchor="middle">Velvet Hearth Co</text>
      <text class="product-type" x="0" y="26" font-size="11" text-anchor="middle">soy candles</text>
    </symbol>
  </defs>

  <!-- colourway set -->
  <g class="colourway-set">
    <use href="#scent-label" class="colourway-magenta" x="58" y="66" width="180" height="180"/>
    <use href="#scent-label" class="colourway-yellow" x="59" y="299" width="172" height="172"/>
    <use href="#scent-label" class="colourway-sky" x="58" y="512" width="174" height="174"/>
    <text class="caption" x="142" y="749" text-anchor="middle">different colourways</text>
    <text class="caption" x="142" y="766" text-anchor="middle">for different scents</text>
  </g>

  <!-- feature label -->
  <g class="feature-label colourway-lime" transform="translate(612 400)">
    <circle class="label-face" cx="0" cy="0" r="268" stroke-width="6"/>
    <text class="scent-ring" font-size="25" letter-spacing="2">
      <textPath href="#large-ring-path" textLength="1480">coconut lime   coconut lime   coconut lime   coconut lime   coconut lime   coconut lime</textPath>
    </text>
    <text class="brand-name" x="0" y="-25" font-size="46" text-anchor="middle">Velvet Hearth Co</text>
    <text class="product-type" x="8" y="58" font-size="25" text-anchor="middle">soy candle</text>
  </g>
  <text class="caption" x="612" y="716" text-anchor="middle">coconut lime version</text>

  <!-- logo usage -->
  <g class="logo-usage">
    <use href="#logo-mark" class="colourway-orange" x="977" y="322" width="152" height="152"/>
    <text class="caption" x="1058" y="512" text-anchor="middle">imagery used as logo</text>
  </g>
</svg>
</body>
</html>
```